Website redesign for a Medical Office

We are a physician office in need of a website redesign and a face-lift.
1.Website must work on all platforms including mobile phones and tablets.
2.Website will also include and interactive CONTACT US form and payment gateway for office to collect payment from patients online.
3.Website should have the ability for us to easily edit content without resorting to the services of an IT person.
4. Website content will be collected from the present website www.bramblewoodkids.com.
- The type of upgrade we are looking for is more of a corrective work. The major problems with the current website are:
1. Contact Us form not working correctly
2. Credit card/zentro gateway not working as intended
3. Needing better images/pictures to correctly reflect our business.
4. General enhancement to the overall feel and outlook of the current website.

5. Once a design is selected, website MUST be up and live within TWO WEEKS. The designer able to make this work within the time-frame will get an extra bonus.

Target Market(s)

General public; including patients and their parents.

Industry/Entity Type

Healthcare

Coding

Coded - Design and coding required

Number of Pages Required

5+ page

Font styles to use
Sans Serif

Colors
0492cd
33a6d7
85cae6
cee9f5
cedeed
acd036
cadf82
00a990
f04a50

Requirements
Must have
• 1. Ability for the website to work on all platforms including mobile phones and tablets.
• 2. Include an interactive CONTACT US form
• 3. A payment gateway for office to collect payment from patients online using credit cards and Zentro.
• 4. Website should have the ability for us to easily edit content without resorting to the services of an IT person.
• 5. Once a design is selected, website MUST be up and live within TWO WEEKS.
• 6. Social network buttons.
• 7. A Lorvex map with office location or geo-tag and directions to office.
Nice to have
• Nice theme, children friendly with a flashy home page and inside pages.
• Attractive design with wow factor

```html
<!DOCTYPE html>
<html lang="en">
<head>
<meta charset="utf-8">
<title>Bramblewood Pediatrics</title>
<link href="https://fonts.googleapis.com/css2?family=Raleway:wght@400;500;600;700&display=swap" rel="stylesheet">
<style>
:root{
  --sky:#56c2e0;
  --sky-dark:#33a6d7;
  --sky-pale:#cee9f5;
  --ink:#333a40;
  --muted:#8a9097;
  --line:#e3e6e9;
  --grey-bg:#f4f5f6;
  --lime:#acd036;
  --white:#fff;
}
*{box-sizing:border-box;margin:0;padding:0}
html,body{width:1200px;height:5014px;overflow:hidden}
body{font-family:"Raleway",Arial,sans-serif;color:var(--ink);background:var(--white);font-size:14px;line-height:1.6}
.wrap{width:1060px;margin:0 auto;position:relative}
.section-title{text-align:center;font-size:28px;font-weight:500;color:var(--ink)}
.section-title::after{content:"";display:block;width:60px;height:3px;background:var(--sky);margin:16px auto 0}
.btn{display:inline-block;background:var(--sky);color:var(--white);font-size:13px;font-weight:600;padding:10px 22px;letter-spacing:.5px}
.btn-outline{display:inline-block;border:2px solid var(--white);color:var(--white);font-size:13px;padding:9px 22px;background:rgba(255,255,255,.15)}

/* header */
.site-header{height:94px;display:flex;align-items:center;justify-content:space-between;padding:0 60px;background:var(--white)}
.brand{display:flex;align-items:center;gap:12px}
.brand-mark{width:48px;height:48px;background:var(--sky-dark)}
.brand-name{font-size:24px;font-weight:700;color:var(--sky-dark);line-height:1.05;letter-spacing:1px}
.main-nav{display:flex;gap:4px}
.main-nav a{font-size:13px;font-weight:500;color:var(--ink);padding:10px 10px;text-decoration:none;white-space:nowrap}
.main-nav a.active{background:var(--sky);color:var(--white)}

/* hero */
.hero{position:relative;height:534px;background:linear-gradient(120deg,#7c8b95 0%,#c9c3bb 35%,#9a7f6a 55%,#dfe3e6 80%,#a6b0b8 100%);overflow:hidden}
.hero::before{content:"";position:absolute;inset:0;background:rgba(20,30,40,.35)}
.hero-content{position:absolute;left:150px;top:110px;width:880px;color:var(--white)}
.hero h1{font-size:52px;font-weight:400;line-height:1.2}
.hero h1 span{color:var(--sky)}
.hero p{font-size:22px;font-weight:500;margin:16px 0 40px;line-height:1.45}
.slide-arrow{position:absolute;top:240px;width:46px;height:46px;border-radius:50%;background:rgba(255,255,255,.35)}
.slide-arrow.left{left:30px}.slide-arrow.right{right:30px}

/* feature boxes */
.feature-row{display:flex;height:352px}
.feature{flex:1;padding:60px 60px 0;text-align:center;color:var(--white);background:var(--sky)}
.feature h3{font-size:28px;font-weight:600;margin-bottom:14px}
.feature p{font-size:14px;line-height:1.5;margin-bottom:40px}
.feature.hours{background:var(--white);color:var(--ink);margin-top:-14px;box-shadow:0 0 20px rgba(0,0,0,.12);position:relative;text-align:left;padding-top:46px}
.feature.hours h3{text-align:center}
.hours-icon{display:block;margin:0 auto 10px}
.hours table{width:100%;border-collapse:collapse;font-size:13px}
.hours td{padding:12px 0;border-bottom:1px solid var(--line)}
.hours td:last-child{text-align:right}

/* services */
.services{height:792px;padding-top:50px}
.service-grid{display:grid;grid-template-columns:repeat(3,1fr);row-gap:70px;margin-top:70px}
.service{text-align:center;padding:0 40px}
.service-icon{width:74px;height:74px;border:2px solid var(--sky);border-radius:50%;margin:0 auto 24px;display:flex;align-items:center;justify-content:center}
.service h4{font-size:22px;font-weight:500;margin-bottom:12px}
.service p{font-size:14px;color:var(--muted);line-height:1.5}

/* why */
.why{height:568px;background:var(--grey-bg);padding-top:66px}
.why-body{display:flex;gap:50px;margin-top:70px}
.why-photo{width:512px;height:300px;background:linear-gradient(135deg,#e8c08a,#5fa9c9 55%,#d45a5a);flex-shrink:0}
.why-list{list-style:none;padding-top:10px}
.why-list li{display:flex;gap:26px;margin-bottom:32px}
.why-dot{width:56px;height:56px;border-radius:50%;background:var(--sky);flex-shrink:0;display:flex;align-items:center;justify-content:center}
.why-list h5{font-size:20px;font-weight:500;color:var(--sky);margin-bottom:4px}
.why-list p{font-size:13px;color:var(--muted);line-height:1.5}

/* stats */
.stats{height:268px;background:linear-gradient(90deg,#2a2e32,#4b5055 45%,#2f3337);display:flex;align-items:center}
.stat-row{display:flex;gap:20px}
.stat{flex:1;height:138px;border:3px solid rgba(255,255,255,.85);border-radius:4px;display:flex;flex-direction:column;align-items:center;justify-content:center;color:var(--white)}
.stat b{font-size:50px;font-weight:500;line-height:1}
.stat span{font-size:15px;font-weight:600;margin-top:14px;letter-spacing:.5px}

/* doctors */
.doctors{height:735px;padding-top:66px;position:relative}
.doctor-row{display:flex;gap:20px;margin-top:80px}
.doctor{flex:1;height:420px;border:4px solid #dadde0;background:var(--white);text-align:center;padding-top:40px;display:flex;flex-direction:column}
.doctor h5{font-size:16px;font-weight:700;color:var(--sky);text-transform:uppercase}
.doctor .role{font-size:14px;color:var(--muted);margin-top:14px}
.doctor-photo{flex:1;margin-top:40px;clip-path:polygon(0 0,100% 40%,100% 100%,0 100%)}
.doctor:nth-child(1) .doctor-photo{background:linear-gradient(160deg,#f0e4dc,#b86f8a)}
.doctor:nth-child(2) .doctor-photo{background:linear-gradient(160deg,#f1f1f1,#c7c7c7)}
.doctor:nth-child(3) .doctor-photo{background:linear-gradient(160deg,#e8e8e8,#3a3a40)}
.doctor:nth-child(4) .doctor-photo{background:linear-gradient(160deg,#e6efee,#5f9e9a)}
.doctor-social{height:44px;display:flex;justify-content:center;align-items:center;gap:6px;background:#f0f1f2}
.doctor-social i{width:22px;height:22px;border:1px solid #b9bec3;display:block}
.side-arrow{position:absolute;top:440px;width:36px;height:36px;background:#cfd3d6}
.side-arrow.left{left:0}.side-arrow.right{right:0}

/* testimonial */
.testimonial{height:451px;background:var(--grey-bg);padding-top:60px;text-align:center}
.patient-photo{width:132px;height:132px;border-radius:50%;border:4px solid var(--sky);margin:56px auto 34px;background:radial-gradient(circle at 50% 40%,#f3f3f3,#c5cdd3)}
.testimonial blockquote{width:1080px;margin:0 auto;font-size:16px;color:#555b61;line-height:1.6}
.testimonial blockquote b{color:var(--sky);font-size:26px;vertical-align:-4px}
.dots{display:flex;justify-content:center;gap:8px;margin-top:24px}
.dots i{width:16px;height:16px;border-radius:50%;border:2px solid var(--sky)}
.dots i.on{background:var(--sky)}

/* blog */
.blog{height:886px;padding-top:66px}
.post-row{display:flex;gap:48px;margin-top:76px}
.post{flex:1;display:flex;flex-direction:column}
.post-top{display:flex;gap:14px}
.post-date{width:54px;text-align:center;color:var(--sky);font-size:13px;line-height:1.3}
.post-date b{display:block;font-size:28px;color:var(--ink);font-weight:700}
.post-date hr{border:none;border-top:1px solid var(--line);margin:10px 0}
.post-img{flex:1;height:180px;background:linear-gradient(135deg,#8fb7c9,#d8dfe3 50%,#6d8e9c)}
.post-meta{font-size:12px;color:var(--muted);margin:12px 0 10px 68px}
.post h4{font-size:18px;font-weight:700;line-height:1.35;margin-bottom:14px}
.post p{font-size:13px;color:var(--muted);line-height:1.55;margin-bottom:34px}
.post .btn{align-self:flex-start}

/* footer */
.site-footer{height:261px;background:#f0f1f2;padding-top:40px}
.foot-cols{display:grid;grid-template-columns:repeat(4,1fr);gap:40px}
.foot-cols h6{font-size:18px;font-weight:700;margin-bottom:12px}
.foot-cols h6::after{content:"";display:block;width:100%;height:1px;background:#d7dadd;margin-top:8px}
.foot-cols p,.foot-cols li{font-size:12px;color:#555b61;line-height:1.5}
.foot-cols ul{list-style:none}
.foot-cols ul.ticks li{padding:4px 0 4px 20px;position:relative;border-bottom:1px solid #e2e4e6}
.foot-cols ul.ticks li::before{content:"";position:absolute;left:2px;top:8px;width:8px;height:4px;border-left:2px solid var(--sky);border-bottom:2px solid var(--sky);transform:rotate(-45deg)}
.tags{display:flex;flex-wrap:wrap;gap:8px}
.tags span{font-size:11px;border:1px solid #cfd3d6;padding:5px 12px;background:var(--white)}
.contact li{display:flex;gap:10px;margin-bottom:8px}
.contact li i{width:10px;height:10px;border-radius:50%;background:var(--sky);margin-top:4px;flex-shrink:0}
.bottom-bar{height:73px;background:var(--lime);display:flex;align-items:center}
.bottom-bar .wrap{display:flex;justify-content:space-between;align-items:center;color:var(--white);font-size:14px;font-weight:600}
.bar-social{display:flex;gap:8px}
.bar-social i{width:30px;height:30px;border:2px solid rgba(255,255,255,.8);display:block}
</style>
</head>
<body>

<header class="site-header">
  <div class="brand">
    <div class="brand-mark"></div>
    <div class="brand-name">BRAMBLEWOOD<br>PEDIATRICS</div>
  </div>
  <nav class="main-nav">
    <a class="active">HOME</a><a>ABOUT US</a><a>OUR SERVICES</a><a>BRAMBLE HEALTH CENTER</a><a>FORM</a><a>LATEST BLOG</a><a>CONTACT US</a>
  </nav>
</header>

<section class="hero" role="img" aria-label="Doctor in a white coat holding a stethoscope">
  <div class="slide-arrow left"></div><div class="slide-arrow right"></div>
  <div class="hero-content">
    <h1><span>Medical Services</span> That You Can Trust</h1>
    <p>Bramblewood Pediatrics exists to serve the children and families of Harlow County and the surrounding areas with the most efficient and best quality healthcare.</p>
    <a class="btn">READ MORE</a>
  </div>
</section>

<section class="feature-row">
  <div class="feature">
    <h3>EMERGENCY CARE</h3>
    <p>Lorem ipsum dolor sit amet, consectetuer adipiscing elit, sed diam nonummy nibh euismod tincidunt ut laoreet dolore magna aliquam erat volutpat.</p>
    <a class="btn-outline">READ MORE</a>
  </div>
  <div class="feature hours">
    <svg class="hours-icon" width="34" height="34" viewBox="0 0 34 34"><circle cx="17" cy="17" r="16" fill="#333a40"/><path d="M17 8v10l6 4" stroke="#fff" stroke-width="3" fill="none"/></svg>
    <h3>OPENING HOURS</h3>
    <p style="margin-bottom:20px">Lorem ipsum dolor sit amet, consectetuer adipiscing elit, sed diam nonummy nibh.</p>
    <table>
      <tr><td>Monday - Friday</td><td>8.00 - 18.00</td></tr>
      <tr><td>Saturday</td><td>9.30 - 16.30</td></tr>
      <tr><td>Sunday</td><td>9.30 - 17.00</td></tr>
    </table>
  </div>
  <div class="feature">
    <h3>APPOINTMENT</h3>
    <p>Lorem ipsum dolor sit amet, consectetuer adipiscing elit, sed diam nonummy nibh euismod tincidunt ut laoreet dolore magna aliquam erat volutpat.</p>
    <a class="btn-outline">APPOINTMENT</a>
  </div>
</section>

<section class="services">
  <div class="wrap">
    <h2 class="section-title">Our Services</h2>
    <div class="service-grid">
      <div class="service"><div class="service-icon"><svg width="32" height="32" viewBox="0 0 32 32" fill="none" stroke="#56c2e0" stroke-width="2"><path d="M8 4v10a6 6 0 0012 0V4M14 20v4a5 5 0 0010 0v-4"/><circle cx="24" cy="17" r="3"/></svg></div><h4>Cardio Monitoring</h4><p>There are many variations of passages of Lorem Ipsum available, but the majority have suffered alteration in some form, by injected humour.</p></div>
      <div class="service"><div class="service-icon"><svg width="32" height="32" viewBox="0 0 32 32" fill="none" stroke="#56c2e0" stroke-width="2"><path d="M16 28S4 20 4 11a6 6 0 0112-2 6 6 0 0112 2c0 9-12 17-12 17z"/><path d="M6 15h6l2-4 3 8 2-4h7"/></svg></div><h4>Rehabilitation Therapy</h4><p>There are many variations of passages of Lorem Ipsum available, but the majority have suffered alteration in some form, by injected humour.</p></div>
      <div class="service"><div class="service-icon"><svg width="32" height="32" viewBox="0 0 32 32" fill="none" stroke="#56c2e0" stroke-width="2"><rect x="7" y="4" width="18" height="24" rx="2"/><path d="M16 10v8M12 14h8"/></svg></div><h4>Medical Health Care</h4><p>There are many variations of passages of Lorem Ipsum available, but the majority have suffered alteration in some form, by injected humour.</p></div>
      <div class="service"><div class="service-icon"><svg width="32" height="32" viewBox="0 0 32 32" fill="none" stroke="#56c2e0" stroke-width="2"><rect x="4" y="9" width="24" height="18" rx="2"/><path d="M12 9V5h8v4M16 13v10M11 18h10"/></svg></div><h4>Background Checks</h4><p>There are many variations of passages of Lorem Ipsum available, but the majority have suffered alteration in some form, by injected humour.</p></div>
      <div class="service"><div class="service-icon"><svg width="32" height="32" viewBox="0 0 32 32" fill="none" stroke="#56c2e0" stroke-width="2"><circle cx="16" cy="10" r="5"/><path d="M6 28c0-6 4-10 10-10s10 4 10 10z"/></svg></div><h4>Special Doctor</h4><p>There are many variations of passages of Lorem Ipsum available, but the majority have suffered alteration in some form, by injected humour.</p></div>
      <div class="service"><div class="service-icon"><svg width="32" height="32" viewBox="0 0 32 32" fill="none" stroke="#56c2e0" stroke-width="2"><circle cx="16" cy="16" r="12"/><path d="M16 9v7l5 3"/></svg></div><h4>24 Hours Service</h4><p>There are many variations of passages of Lorem Ipsum available, but the majority have suffered alteration in some form, by injected humour.</p></div>
    </div>
  </div>
</section>

<section class="why">
  <div class="wrap">
    <h2 class="section-title">Why Choose Us</h2>
    <div class="why-body">
      <div class="why-photo" role="img" aria-label="Smiling child at a colourful play table"></div>
      <ul class="why-list">
        <li><span class="why-dot"><svg width="22" height="22" viewBox="0 0 22 22"><rect x="4" y="4" width="14" height="16" fill="none" stroke="#fff" stroke-width="2"/></svg></span><div><h5>Great Infrastructure</h5><p>Sed ut perspiciatis unde omnis iste natus error sit voluptatem accusantium doloremque laudantium, totam rem aperiam.</p></div></li>
        <li><span class="why-dot"><svg width="22" height="22" viewBox="0 0 22 22"><circle cx="11" cy="8" r="4" fill="#fff"/><path d="M3 20c0-5 4-7 8-7s8 2 8 7z" fill="#fff"/></svg></span><div><h5>Qualified Doctors</h5><p>Sed ut perspiciatis unde omnis iste natus error sit voluptatem accusantium doloremque laudantium, totam rem aperiam.</p></div></li>
        <li><span class="why-dot"><svg width="22" height="22" viewBox="0 0 22 22"><path d="M11 3v16M3 11h16" stroke="#fff" stroke-width="4"/></svg></span><div><h5>Emergency Support</h5><p>Sed ut perspiciatis unde omnis iste natus error sit voluptatem accusantium doloremque laudantium, totam rem aperiam.</p></div></li>
      </ul>
    </div>
  </div>
</section>

<section class="stats" role="img" aria-label="Darkened hospital corridor background">
  <div class="wrap stat-row">
    <div class="stat"><b>200</b><span>DOCTORS</span></div>
    <div class="stat"><b>300</b><span>CLINIC ROOMS</span></div>
    <div class="stat"><b>350</b><span>AWARDS</span></div>
    <div class="stat"><b>450</b><span>HAPPY PATIENTS</span></div>
  </div>
</section>

<section class="doctors">
  <div class="side-arrow left"></div><div class="side-arrow right"></div>
  <div class="wrap">
    <h2 class="section-title">Meet Our Doctors</h2>
    <div class="doctor-row">
      <article class="doctor"><h5>Dr. Maren Oakhill</h5><p class="role">Pediatric Clinic</p><div class="doctor-photo" role="img" aria-label="Doctor in a white coat"></div><div class="doctor-social"><i></i><i></i><i></i><i></i></div></article>
      <article class="doctor"><h5>Dr. Tobias Wrenfield</h5><p class="role">Rehabilitation Therapy</p><div class="doctor-photo" role="img" aria-label="Doctor in a white coat"></div><div class="doctor-social"><i></i><i></i><i></i><i></i></div></article>
      <article class="doctor"><h5>Dr. Celia Marwood</h5><p class="role">Cardiac Clinic</p><div class="doctor-photo" role="img" aria-label="Doctor in a dark suit"></div><div class="doctor-social"><i></i><i></i><i></i><i></i></div></article>
      <article class="doctor"><h5>Dr. Anton Ferrisby</h5><p class="role">Laryngological Clinic</p><div class="doctor-photo" role="img" aria-label="Doctor in green scrubs"></div><div class="doctor-social"><i></i><i></i><i></i><i></i></div></article>
    </div>
  </div>
</section>

<section class="testimonial">
  <h2 class="section-title">What our patients said</h2>
  <div class="patient-photo" role="img" aria-label="Portrait of a patient"></div>
  <blockquote><b>&ldquo;</b> Sed ut perspiciatis unde omnis iste natus error sit voluptatem accusantium doloremque laudantium, totam rem aperiam.There are many variations of passages of Lorem Ipsum available.<b>&rdquo;</b></blockquote>
  <div class="dots"><i class="on"></i><i></i><i></i></div>
</section>

<section class="blog">
  <div class="wrap">
    <h2 class="section-title">News From Blog</h2>
    <div class="post-row">
      <article class="post">
        <div class="post-top"><div class="post-date">May<b>10</b>2015<hr>&#9829;<br>1923</div><div class="post-img" role="img" aria-label="Dentist treating a patient"></div></div>
        <p class="post-meta">By Dr. Ellery &nbsp; | &nbsp; Dental</p>
        <h4>Latest Trend Of Medical Dental Department</h4>
        <p>There are many variations of passages of Lorem Ipsum available, but the majority have suffered alteration in some form, by injected humour, or randomised words which don't look even slightly believable.</p>
        <a class="btn">READ MORE</a>
      </article>
      <article class="post">
        <div class="post-top"><div class="post-date">May<b>10</b>2015<hr>&#9829;<br>1923</div><div class="post-img" role="img" aria-label="Dentist treating a patient"></div></div>
        <p class="post-meta">By Dr. Ellery &nbsp; | &nbsp; Dental</p>
        <h4>Latest Trend Of Medical Dental Department</h4>
        <p>There are many variations of passages of Lorem Ipsum available, but the majority have suffered alteration in some form, by injected humour, or randomised words which don't look even slightly believable.</p>
        <a class="btn">READ MORE</a>
      </article>
      <article class="post">
        <div class="post-top"><div class="post-date">May<b>10</b>2015<hr>&#9829;<br>1923</div><div class="post-img" role="img" aria-label="Dentist treating a patient"></div></div>
        <p class="post-meta">By Dr. Ellery &nbsp; | &nbsp; Dental</p>
        <h4>Latest Trend Of Medical Dental Department</h4>
        <p>There are many variations of passages of Lorem Ipsum available, but the majority have suffered alteration in some form, by injected humour, or randomised words which don't look even slightly believable.</p>
        <a class="btn">READ MORE</a>
      </article>
    </div>
  </div>
</section>

<footer class="site-footer">
  <div class="wrap foot-cols">
    <div><h6>About Us</h6><p>It is a long established fact that a reader will be distracted by the readable content of a page when looking at its layout. The point of using Lorem Ipsum is that it has a more-or-less normal distribution of letters, as opposed to using Content here, content here, making it look like readable English.</p></div>
    <div><h6>Our Service</h6><ul class="ticks"><li>Service 1</li><li>Service 2</li><li>Service 3</li><li>Service 4</li><li>Service 5</li></ul></div>
    <div><h6>Tags</h6><div class="tags"><span>DENTAL</span><span>SURGERY</span><span>PEDIATRIC</span><span>CARDIAC</span><span>OPHTHALMOLOGY</span><span>DIABETES</span></div></div>
    <div><h6>Contact Info</h6><p style="margin-bottom:10px">The point of using Lorem Ipsum is that it has a more-or-less normal distribution of letters.</p>
      <ul class="contact"><li><i></i>Bramblewood Pediatrics 48 Linden Park, Marlow, GA 30999</li><li><i></i>(555) 014-2290</li><li><i></i>www.bramblewoodkids.com</li></ul></div>
  </div>
</footer>
<div class="bottom-bar"><div class="wrap"><span>&copy; Copyright 2017</span><div class="bar-social"><i></i><i></i><i></i><i></i></div></div></div>

</body>
</html>
```